24/7 Gym Membership Pricing Card (A6)

I need a pricing card with the different membership options on it.

The membership options are;

12 Month Minimum Term:
No Joining Fee, $25 Access Card Fee, $12.25 per week

No Contract:
$89 Joining Fee, $55 Access Card Fee, $13.50 per week

Pay in Advance:
12 Month - $540
6 Month - $295
3 Month - $190

I have attached our old pricing card below for reference.

Our Logo is also attached.

Target Market(s)

Potential members

Industry/Entity Type

Fitness

Colors
f37122
f68e4e
f9bb94
f78f20
faa54b
fbc994

Requirements
Must have
• My Logo, pricing options
Nice to have
• Contact details; 4158 2293, hollis@vantorafit.com.au, www.vantorafit.com.au
• Our staffed hours; Mon-Thur: 12pm - 7pm, Fri-Sat: 8am - 1pm
Should not have
• Wasted space

```html
<!DOCTYPE html>
<html lang="en">
<head>
<meta charset="utf-8">
<title>Vantora Fit Hollis – Membership Options</title>
<link rel="stylesheet" href="https://fonts.googleapis.com/css2?family=Arimo:wght@400;700&display=swap">
<style>
  :root {
    --orange: #f37122;
    --orange-box: #f78f20;
    --orange-soft: #f68e4e;
    --orange-pale: #faa54b;
    --white: #ffffff;
    --page: #ffffff;
    --photo-dark: #3a2216;
    --photo-mid: #8a4a26;
    --photo-warm: #d98a52;
    --photo-light: #f1cfae;
  }
  * { box-sizing: border-box; margin: 0; padding: 0; }
  html, body {
    width: 1200px; height: 1200px; overflow: hidden;
    background: var(--page);
    font-family: "Arimo", Arial, sans-serif;
    color: var(--white);
  }
  .pricing-card {
    position: absolute; left: 16px; top: 210px;
    width: 1146px; height: 814px;
    overflow: hidden;
    background: var(--orange-box);
    box-shadow: 8px 10px 14px rgba(0,0,0,0.28);
  }
  .hero-photo {
    position: absolute; left: 0; top: 0; width: 1146px; height: 662px;
    background:
      radial-gradient(ellipse 360px 300px at 560px 180px, var(--photo-light) 0%, rgba(241,207,174,0) 70%),
      radial-gradient(ellipse 300px 260px at 960px 260px, var(--photo-warm) 0%, rgba(217,138,82,0) 75%),
      linear-gradient(100deg, var(--photo-dark) 0%, var(--photo-mid) 35%, var(--photo-warm) 60%, var(--photo-mid) 100%);
  }
  .title-badge {
    position: absolute; left: 820px; top: 0; width: 328px; height: 168px;
    border-radius: 50%; background: var(--orange-box);
    display: flex; align-items: center; justify-content: center;
    text-align: center; font-size: 41px; line-height: 1.25;
  }
  .plan-badge {
    position: absolute; width: 156px; height: 156px; border-radius: 50%;
    background: var(--orange-box);
    display: flex; flex-direction: column; align-items: center; justify-content: center;
    text-align: center; z-index: 2;
  }
  .plan-badge--term { left: 2px; top: 210px; flex-direction: row; gap: 4px; }
  .plan-badge--term .term-number { font-size: 54px; letter-spacing: -4px; margin-left: -36px; }
  .plan-badge--term .term-label { font-size: 24px; line-height: 1.02; letter-spacing: -1px; text-align: right; }
  .plan-badge--flex { left: 364px; top: 212px; }
  .plan-badge--flex .flex-big { font-size: 78px; line-height: 0.9; letter-spacing: -3px; }
  .plan-badge--flex .flex-small { font-size: 26px; }
  .plan-badge--advance { left: 750px; top: 221px; font-size: 31px; line-height: 1.05; }

  .price-box {
    position: absolute; background: var(--orange-box);
    text-align: center;
    box-shadow: 0 -3px 6px rgba(0,0,0,0.18);
    display: flex; flex-direction: column; align-items: center; justify-content: center;
  }
  .price-box .amount { font-size: 48px; line-height: 1.05; }
  .price-box .label { font-size: 30px; line-height: 1.1; }
  .row-1 { top: 348px; height: 100px; z-index: 1; }
  .row-2 { top: 448px; height: 108px; z-index: 1; }
  .row-3 { top: 556px; height: 106px; z-index: 1; }
  .col-a.row-1 { left: 66px; width: 250px; }
  .col-a.row-2 { left: 35px; width: 309px; }
  .col-a.row-3 { left: 4px; width: 372px; }
  .col-b.row-1 { left: 448px; width: 250px; }
  .col-b.row-2 { left: 418px; width: 308px; }
  .col-b.row-3 { left: 386px; width: 372px; }
  .col-c.row-1 { left: 830px; width: 248px; }
  .col-c.row-2 { left: 798px; width: 310px; }
  .col-c.row-3 { left: 768px; width: 372px; }
  .card-icon { position: absolute; left: 30px; top: 16px; width: 56px; height: 34px; }
  .col-b.row-2 .amount { margin-left: 0; }

  .info-band {
    position: absolute; left: 0; top: 662px; width: 1146px; height: 152px;
    background: var(--orange-box); font-weight: 700;
  }
  .brand-name {
    position: absolute; left: 26px; top: 34px; width: 290px;
    text-align: center; font-size: 34px; font-weight: 700; line-height: 1.2;
  }
  .brand-name .brand-place { display: block; font-size: 24px; letter-spacing: 12px; }
  .contact-block {
    position: absolute; left: 310px; top: 16px; width: 452px;
    text-align: center; font-size: 26px; line-height: 1.33;
  }
  .hours-block {
    position: absolute; left: 730px; top: 14px; width: 420px;
    font-size: 25px; line-height: 1.33;
  }
  .hours-block .hours-title { position: absolute; left: 0; top: 0; }
  .hours-block .hours-list { position: absolute; left: 158px; top: 2px; width: 250px; text-align: center; }
</style>
</head>
<body>
  <main class="pricing-card">
    <div class="hero-photo" role="img" aria-label="Warm-toned photo of members training on cardio machines in the gym"></div>

    <div class="title-badge">Membership<br>Options</div>

    <div class="plan-badge plan-badge--term">
      <span class="term-number">12</span>
      <span class="term-label">Month<br>Minimum<br>Access</span>
    </div>
    <div class="plan-badge plan-badge--flex">
      <span class="flex-big">No</span>
      <span class="flex-small">Contracts</span>
    </div>
    <div class="plan-badge plan-badge--advance">Pay<br>In<br>Advance</div>

    <div class="price-box col-a row-1"><span class="amount">No</span><span class="label">Joining Fee</span></div>
    <div class="price-box col-a row-2"><span class="amount">$25</span><span class="label">Access Card Fee</span></div>
    <div class="price-box col-a row-3"><span class="amount">$12.25</span><span class="label">Per Week</span></div>

    <div class="price-box col-b row-1"><span class="amount">$89</span><span class="label">Joining&nbsp;&nbsp;Fee</span></div>
    <div class="price-box col-b row-2">
      <svg class="card-icon" viewBox="0 0 56 34" aria-hidden="true">
        <rect x="1" y="1" width="54" height="32" fill="none" stroke="#fff" stroke-width="2"/>
        <circle cx="14" cy="12" r="5" fill="#fff"/>
        <path d="M6 28 q8 -12 16 0 z" fill="#fff"/>
        <rect x="28" y="9" width="22" height="3" fill="#fff"/>
        <rect x="28" y="16" width="22" height="3" fill="#fff"/>
        <rect x="28" y="23" width="22" height="3" fill="#fff"/>
      </svg>
      <span class="amount">$55</span><span class="label">Access Card Fee</span>
    </div>
    <div class="price-box col-b row-3"><span class="amount">$13.50</span><span class="label">Per Week</span></div>

    <div class="price-box col-c row-1"><span class="amount">$540</span><span class="label">12 Month</span></div>
    <div class="price-box col-c row-2"><span class="amount">$295</span><span class="label">6 Month</span></div>
    <div class="price-box col-c row-3"><span class="amount">$190</span><span class="label">3 Month</span></div>

    <footer class="info-band">
      <div class="brand-name">Vantora Fit<span class="brand-place">HOLLIS</span></div>
      <div class="contact-block">
        Contact Details:<br>
        07 4158 2293<br>
        hollis@vantorafit.com.au<br>
        www.vantorafit.com.au
      </div>
      <div class="hours-block">
        <span class="hours-title">Staff hours:</span>
        <span class="hours-list">Monday-Thursdays<br>12:00pm-7:00pm<br>Friday-Saturday<br>8:00am-1:00pm</span>
      </div>
    </footer>
  </main>
</body>
</html>
```